Maple Hollow Bloom Panels Business card

Looking to have a business card design incorporating my logo for my flower wall business.

Industry/Entity Type

Wedding & event planning

Contact Information for Business Card

My business logo, my name - Lena Whitcombe (owner), my tagline - Let us be your something extra, phone # 401-726-3148, email address - maplehollowbloompanels@mailvane.net, my website - maplehollowbloompanels.net, Instagram handle- @maplehollowbloompanels, FB handle Handle - maplehollowbloompanels

Font styles to use
Other font styles liked:
• Sentaina is the font that is used in my logo

Requirements
Must have
• Would like a double sided business card

```html
<!DOCTYPE html>
<html lang="en">
<head>
<meta charset="utf-8">
<title>Maple Hollow Bloom Panels – Business Card</title>
<link href="https://fonts.googleapis.com/css2?family=Work+Sans:wght@400;500;600&family=Caveat+Brush&display=swap" rel="stylesheet">
<style>
  :root {
    --backdrop: #cbcbcb;
    --card-blush: #f3d9e8;
    --brand-pink: #c9287f;
    --accent-pink: #d12882;
    --ink-dark: #2b2b2b;
    --ink-gray: #8a8a8a;
    --gold: #d8ae57;
    --gold-light: #e9cf86;
    --white: #ffffff;
  }
  * { box-sizing: border-box; margin: 0; padding: 0; }
  html, body {
    width: 990px;
    height: 1200px;
    overflow: hidden;
    background: var(--backdrop);
    font-family: "Work Sans", Arial, sans-serif;
  }
  .canvas {
    position: relative;
    width: 990px;
    height: 1200px;
  }
  .card {
    position: absolute;
    left: 178px;
    width: 638px;
    height: 367px;
    border-radius: 30px;
    overflow: hidden;
  }
  .card-front { top: 124px; background: var(--card-blush); }
  .card-back { top: 617px; background: var(--brand-pink); }

  .owner-name {
    position: absolute;
    left: 42px;
    top: 58px;
    font-size: 25px;
    font-weight: 600;
    color: var(--ink-dark);
  }
  .owner-role {
    position: absolute;
    left: 43px;
    top: 89px;
    font-size: 12px;
    font-weight: 500;
    color: var(--accent-pink);
  }
  .gold-rule {
    position: absolute;
    left: 42px;
    top: 110px;
    width: 302px;
    height: 2px;
    background: linear-gradient(90deg, var(--gold), var(--gold-light), var(--gold));
  }
  .contact-line {
    position: absolute;
    left: 42px;
    display: flex;
    align-items: center;
    gap: 8px;
    font-size: 16px;
    color: var(--ink-gray);
  }
  .contact-line svg { width: 14px; height: 14px; }
  .contact-email { top: 133px; }
  .contact-web { top: 158px; }

  .phone-line {
    position: absolute;
    left: 34px;
    top: 206px;
    display: flex;
    align-items: center;
    gap: 10px;
    font-size: 39px;
    font-weight: 400;
    color: var(--accent-pink);
  }
  .phone-line svg { width: 48px; height: 48px; }

  .find-us {
    position: absolute;
    left: 42px;
    top: 282px;
    font-size: 20px;
    color: var(--accent-pink);
  }
  .social-line {
    position: absolute;
    left: 134px;
    display: flex;
    align-items: center;
    gap: 12px;
    font-size: 16px;
    color: var(--accent-pink);
  }
  .social-line .dot {
    width: 26px;
    height: 26px;
    border: 2px solid var(--accent-pink);
    border-radius: 50%;
  }
  .social-instagram { top: 280px; }
  .social-facebook { top: 318px; }

  .brand-badge {
    position: absolute;
    left: 383px;
    top: 81px;
    width: 216px;
    height: 216px;
    border-radius: 50%;
    background: var(--white);
    display: flex;
    align-items: center;
    justify-content: center;
    text-align: center;
    padding: 30px;
  }
  .brand-name {
    font-size: 24px;
    font-weight: 500;
    line-height: 1.25;
    color: var(--accent-pink);
  }

  .tagline {
    position: absolute;
    left: 0;
    right: 0;
    top: 150px;
    text-align: center;
    font-family: "Caveat Brush", "Comic Sans MS", cursive;
    font-size: 50px;
    color: var(--gold);
  }
</style>
</head>
<body>
<main class="canvas">
  <section class="card card-front" aria-label="Business card front">
    <h1 class="owner-name">Lena Whitcombe</h1>
    <p class="owner-role">Owner</p>
    <div class="gold-rule"></div>

    <p class="contact-line contact-email">
      <svg viewBox="0 0 14 14" aria-hidden="true"><rect x="1" y="3" width="12" height="8" rx="1" fill="none" stroke="#d12882" stroke-width="1.6"/><path d="M1.5 3.5 7 8l5.5-4.5" fill="none" stroke="#d12882" stroke-width="1.4"/></svg>
      maplehollowbloompanels@mailvane.net
    </p>
    <p class="contact-line contact-web">
      <svg viewBox="0 0 14 14" aria-hidden="true"><circle cx="8" cy="6" r="4" fill="none" stroke="#d12882" stroke-width="1.6"/><path d="M5 9 1.5 12.5" stroke="#d12882" stroke-width="1.8" stroke-linecap="round"/></svg>
      maplehollowbloompanels.net
    </p>

    <p class="phone-line">
      <svg viewBox="0 0 48 48" aria-hidden="true"><circle cx="24" cy="24" r="21" fill="none" stroke="#d12882" stroke-width="3"/><path d="M17 13c1.5-1 3-.5 3.6.8l1.8 4c.5 1.1.2 2.2-.7 2.9l-1.5 1.1c1 2.6 3.3 5 6 6.2l1.2-1.5c.7-.9 1.9-1.1 2.9-.6l3.9 1.9c1.3.6 1.7 2.2.8 3.5l-1.3 1.9c-1 1.4-2.8 2-4.5 1.5C22 33 15 26 13.4 18.8c-.4-1.7.3-3.4 1.6-4.4z" fill="#d12882"/></svg>
      401-726-3148
    </p>

    <p class="find-us">Find Us |</p>
    <p class="social-line social-instagram"><span class="dot" aria-hidden="true"></span>@maplehollowbloompanels</p>
    <p class="social-line social-facebook"><span class="dot" aria-hidden="true"></span>maplehollowbloompanels</p>

    <div class="brand-badge">
      <p class="brand-name">Maple Hollow Bloom Panels</p>
    </div>
  </section>

  <section class="card card-back" aria-label="Business card back">
    <p class="tagline">Let us be your something extra</p>
  </section>
</main>
</body>
</html>
```